Cat sitting business Web Design Project ***

I have a cat sitting business where I either take care of cats in their home or board them in mine

I need a website which offers my services, my rates, about me, FAQ's, Hours of operation and service areas covered, testimonials, contact info, newsletter sign up, gallery of photos and the ability for me to go in and update when needed.

Coding

Coded - Design and coding required

Number of Pages Required

5+ page

```html
<!DOCTYPE html>
<html lang="en">
<head>
<meta charset="UTF-8">
<title>Whisker Haven Cat Sitting</title>
<link href="https://fonts.googleapis.com/css2?family=Nunito:wght@500;600;700;800;900&display=swap" rel="stylesheet">
<style>
  :root {
    --rose: #c2747b;
    --rose-dark: #b5646c;
    --green: #86c25a;
    --page: #f7f4f3;
    --ink: #6f6a6a;
    --white: #ffffff;
  }
  * { margin: 0; padding: 0; box-sizing: border-box; }
  html, body { width: 1200px; height: 654px; overflow: hidden; }
  body {
    font-family: "Nunito", sans-serif;
    background: var(--page);
    position: relative;
  }
  .topbar {
    position: absolute; left: 0; top: 0; width: 1200px; height: 27px;
    background: var(--rose);
    color: var(--white);
    font-size: 11px; font-weight: 600;
    display: flex; align-items: center;
  }
  .contact-list { display: flex; align-items: center; margin-left: 122px; }
  .contact-item { display: flex; align-items: center; gap: 8px; padding: 0 16px; white-space: nowrap; }
  .contact-item + .contact-item { border-left: 1px solid rgba(255,255,255,.6); }
  .contact-item:first-child { padding-left: 0; }
  .contact-item svg { width: 11px; height: 11px; }
  .social-list { display: flex; gap: 7px; margin-left: auto; margin-right: 84px; }
  .social-dot { width: 13px; height: 13px; border: 1.4px solid var(--white); border-radius: 50%; }

  .site-header {
    position: absolute; left: 0; top: 27px; width: 1200px; height: 80px;
    display: flex; align-items: center;
  }
  .brand { margin-left: 118px; display: flex; align-items: center; gap: 8px; }
  .brand-mark { width: 22px; height: 22px; border-radius: 50%; background: var(--rose); }
  .brand-name { font-size: 12px; font-weight: 700; color: var(--rose); line-height: 1.15; white-space: nowrap; }
  .main-nav { margin-left: auto; margin-right: 85px; display: flex; align-items: center; gap: 46px; font-size: 11px; font-weight: 700; color: var(--ink); }
  .main-nav .is-active { color: var(--green); }
  .nav-cta {
    background: var(--rose); color: var(--white);
    padding: 5px 13px; margin-left: -12px;
    clip-path: polygon(6% 0, 100% 0, 94% 100%, 0 100%);
  }

  .hero-title {
    position: absolute; left: 118px; top: 220px;
    font-size: 50px; font-weight: 900; line-height: 60px;
    color: var(--rose); white-space: nowrap;
  }
  .hero-title .accent { color: var(--green); }
  .hero-actions { position: absolute; left: 118px; top: 431px; display: flex; gap: 20px; }
  .btn { height: 35px; padding: 0 18px; border-radius: 18px; font-size: 12px; font-weight: 800; display: flex; align-items: center; white-space: nowrap; }
  .btn-primary { background: var(--green); color: var(--white); }
  .btn-outline { border: 1.5px solid var(--rose); border-right-color: transparent; border-bottom-color: transparent; color: var(--rose-dark); padding: 0 26px; }

  .photo {
    position: absolute; width: 228px;
    border-radius: 20px;
    border: 5px solid var(--white);
    box-shadow: 0 8px 22px rgba(120,90,90,.22);
  }
  .photo-a { left: 622px; top: 132px; height: 190px; background: linear-gradient(135deg, #d7c9bd, #8b7a6c 55%, #e3d3c8); }
  .photo-b { left: 622px; top: 352px; height: 286px; background: linear-gradient(160deg, #b9c4cd, #d69a5c 50%, #f0ece8); }
  .photo-c { left: 877px; top: 132px; height: 280px; background: linear-gradient(150deg, #6a4a3a, #d9cdc4 50%, #efe9e4); }
  .photo-d { left: 877px; top: 442px; height: 196px; background: linear-gradient(140deg, #c86a4a, #e9d2c2 55%, #b98a6e); }
</style>
</head>
<body>
  <div class="topbar">
    <div class="contact-list">
      <span class="contact-item">
        <svg viewBox="0 0 12 12"><path d="M2.5 1l2 2.5-1.2 1.2a7 7 0 0 0 4 4L8.5 7.5 11 9.5 9.8 11C5 11 1 7 1 2.2z" fill="#fff"/></svg>
        555-018-2046
      </span>
      <span class="contact-item">
        <svg viewBox="0 0 12 12"><rect x="1" y="2.5" width="10" height="7" fill="none" stroke="#fff" stroke-width="1.2"/><path d="M1 2.5l5 4 5-4" fill="none" stroke="#fff" stroke-width="1.2"/></svg>
        hello@whiskerhaven.test
      </span>
      <span class="contact-item">
        <svg viewBox="0 0 12 12"><circle cx="6" cy="6" r="5" fill="none" stroke="#fff" stroke-width="1.2"/><path d="M6 3v3l2 1.5" fill="none" stroke="#fff" stroke-width="1.2"/></svg>
        Your Email Here
      </span>
    </div>
    <div class="social-list">
      <span class="social-dot"></span><span class="social-dot"></span><span class="social-dot"></span>
      <span class="social-dot"></span><span class="social-dot"></span><span class="social-dot"></span>
    </div>
  </div>

  <header class="site-header">
    <div class="brand">
      <span class="brand-mark"></span>
      <span class="brand-name">Whisker Haven<br>Cat Sitting</span>
    </div>
    <nav class="main-nav">
      <span class="is-active">Home</span>
      <span>About</span>
      <span>Services</span>
      <span>Pricings</span>
      <span>FAQs</span>
      <span>Blogs</span>
      <span class="nav-cta">Contact Me</span>
    </nav>
  </header>

  <h1 class="hero-title">Devoted to Proper<br><span class="accent">Cat Sitting</span><br>Services</h1>
  <div class="hero-actions">
    <span class="btn btn-primary">View Services</span>
    <span class="btn btn-outline">Contact Me</span>
  </div>

  <div class="photo photo-a" role="img" aria-label="Tabby kitten being stroked under the chin"></div>
  <div class="photo photo-b" role="img" aria-label="Ginger cat sleeping on a white blanket"></div>
  <div class="photo photo-c" role="img" aria-label="White and ginger cat relaxing on a lap"></div>
  <div class="photo photo-d" role="img" aria-label="Cat sitter cuddling a cat"></div>
</body>
</html>
```